Lantern Hollow Distillery Rum Label Project

We are a new distillery opening up in the old train station in Mount Holly, NJ. We will be making rum, gin, and vodka in the first year of operation, and hope to expand to other products in the future. We need label designs for our brand "Lantern Hollow Rum TM" that complies with QFR regulations including items such as UPC, surgeon general warning, font size requirement, volume, proof, ect. For further information regarding the labeling requirements for all the legal stuff: https://www.qfrexample.org/liquor/kpm/section1.pdf
Updates

We will also need a tamper evident seal. Simple is fine.

Target Market(s)

25-35 casual cocktail drinkers, 35-65 craft spirit enthusiasts, all legal ages local craft market celebrants

Font styles to use
Serif
Sans Serif
Decorative

Colors

Designer to choose colors to be used in the design.

Requirements
Must have
• Must adhere to QFR guidelines https://www.qfrexample.org/liquor/kpm/section1.pdf
• Gold foiling-- don't bleed with foil to prevent foil edges from curling
Nice to have
• References to Mount Holly, 1800s, trains, signage, maps, tickets, history, motto: "All Aboard!"
Should not have
• References to "getting wrecked". The brand is more tongue in cheek and playful.

```html
<!DOCTYPE html>
<html lang="en">
<head>
<meta charset="utf-8">
<title>Copper Whistle Vodka Label</title>
<link href="https://fonts.googleapis.com/css2?family=Old+Standard+TT:wght@400;700&family=Oswald:wght@600&display=swap" rel="stylesheet">
<style>
  :root {
    --glass: #b4b9c0;
    --glass-light: #c3c7cd;
    --gold: #b98d22;
    --gold-muted: #8f7538;
    --paper: #ecebe8;
    --ink: #1d1d1d;
    --red: #d4262a;
  }
  * { margin: 0; padding: 0; box-sizing: border-box; }
  html, body { width: 1200px; height: 900px; overflow: hidden; }
  body {
    background: radial-gradient(ellipse at 50% 45%, var(--glass-light), var(--glass) 70%);
    font-family: "Old Standard TT", serif;
    color: var(--ink);
    position: relative;
  }
  .label {
    position: absolute;
    left: 0; top: 0; width: 1200px; height: 900px;
  }
  .tagline {
    position: absolute; top: 92px; width: 100%;
    text-align: center; color: var(--gold-muted);
    font-size: 26px; letter-spacing: 10px;
  }
  .brand {
    position: absolute; top: 170px; width: 100%;
    display: flex; justify-content: center; align-items: center; gap: 26px;
  }
  .brand-dot {
    width: 64px; height: 64px; border-radius: 50%;
    background: var(--gold);
  }
  .brand-name {
    font-family: "Oswald", sans-serif; font-weight: 600;
    font-size: 92px; letter-spacing: 4px; color: var(--gold);
    text-transform: uppercase;
  }
  .product-line {
    position: absolute; top: 352px; width: 100%;
    display: flex; justify-content: center; align-items: baseline; gap: 10px;
    color: var(--gold-muted);
  }
  .product-line .note { font-family: "Oswald", sans-serif; font-weight: 600; font-size: 24px; letter-spacing: 3px; opacity: .85; }
  .product-line .spirit { font-size: 56px; letter-spacing: 8px; color: var(--gold-muted); }
  .bottler {
    position: absolute; top: 428px; width: 100%;
    text-align: center; color: var(--gold-muted); line-height: 1.5;
  }
  .bottler .small { font-size: 15px; letter-spacing: 3px; }
  .bottler .maker { font-size: 19px; letter-spacing: 3px; font-weight: 700; }
  .strip {
    position: absolute; left: 205px; top: 530px; width: 790px; height: 270px;
    background: var(--paper);
    padding: 26px 34px 0 34px;
  }
  .strip-head {
    display: flex; align-items: flex-end;
    border-bottom: 3px solid var(--ink); padding-bottom: 6px;
  }
  .strip-head .class { font-size: 34px; letter-spacing: 3px; font-weight: 700; padding-right: 18px; border-right: 3px solid var(--ink); }
  .strip-head .batch-label { font-size: 12px; margin: 0 14px 0 14px; align-self: flex-start; }
  .strip-head .batch { font-size: 34px; color: var(--red); letter-spacing: 1px; }
  .strip-body {
    font-size: 18px; line-height: 1.45; padding: 10px 0 10px;
    border-bottom: 3px solid var(--ink);
  }
  .strip-body b { font-weight: 700; }
  .strip-body i { font-style: italic; }
  .strip-foot { display: flex; align-items: stretch; height: 62px; }
  .strip-foot .stat { font-size: 30px; font-weight: 700; padding: 12px 16px 0 0; border-right: 3px solid var(--ink); margin-right: 16px; }
  .strip-foot .signoff { display: flex; align-items: flex-start; gap: 8px; padding-top: 6px; }
  .strip-foot .signoff-label { font-size: 12px; }
  .signature {
    width: 230px; height: 44px;
    background: linear-gradient(90deg, rgba(212,38,42,.18), rgba(212,38,42,.08));
  }
</style>
</head>
<body>
<main class="label">
  <p class="tagline">organic craft</p>

  <div class="brand">
    <span class="brand-dot"></span>
    <span class="brand-name">Copper Whistle</span>
  </div>

  <p class="product-line">
    <span class="note">Distilled</span>
    <span class="spirit">VODKA</span>
    <span class="note">six times</span>
  </p>

  <div class="bottler">
    <p class="small">Distilled and bottled by</p>
    <p class="maker">Lantern Hollow</p>
  </div>

  <section class="strip">
    <div class="strip-head">
      <span class="class">Neutral Spirit</span>
      <span class="batch-label">Batch No.</span>
      <span class="batch">01/023/2017</span>
    </div>
    <p class="strip-body">
      Small-batch spirit <b>distilled six times from organic grain</b> in the old station house,
      then filtered slowly through charcoal <i>for a clean, bright finish worth the trip.</i>
    </p>
    <div class="strip-foot">
      <span class="stat">42% vol.</span>
      <span class="stat">90 Proof</span>
      <div class="signoff">
        <span class="signoff-label">Master Distiller</span>
        <div class="signature" role="img" aria-label="Handwritten signature of the master distiller in red ink"></div>
      </div>
    </div>
  </section>
</main>
</body>
</html>
```